I need a design to display a result on a range line

For example - If I have a blood sugar result and I want to display it on a line so that I can display it in picture terms so that it can be understood more.
I want to input the result in a calculator so it can be displayed on the range line.

I want it so I can customise it and apply it to other results my self too.

```html
<!DOCTYPE html>
<html lang="en">
<head>
<meta charset="utf-8">
<title>Blood Glucose Level Range</title>
<link rel="stylesheet" href="https://fonts.googleapis.com/css2?family=Oswald:wght@400&family=Roboto:wght@700&display=swap">
<style>
  :root {
    --page-bg: #ffffff;
    --panel-teal: #2fada8;
    --card-white: #ffffff;
    --text-light: #ffffff;
    --text-dark: #1b1b1b;
    --range-low: #3cb514;
    --range-optimal: #f2cf0a;
    --range-pre: #f47f1b;
    --range-high: #e8202a;
    --art-hand-a: #f6d9c3;
    --art-hand-b: #efc9ad;
    --art-meter-a: #e2625f;
    --art-meter-b: #c8504f;
  }
  html, body {
    margin: 0;
    padding: 0;
    width: 1200px;
    height: 1200px;
    overflow: hidden;
    background: var(--page-bg);
  }
  .canvas {
    position: relative;
    width: 1200px;
    height: 1200px;
  }
  .glucose-panel {
    position: absolute;
    left: 38px;
    top: 440px;
    width: 1134px;
    height: 344px;
    background: var(--panel-teal);
    border-radius: 12px;
  }
  .finger-prick-art {
    position: absolute;
    left: 0;
    top: 29px;
    width: 200px;
    height: 87px;
    border-radius: 4px;
    background: linear-gradient(90deg, var(--art-hand-a), var(--art-hand-b));
  }
  .panel-title {
    position: absolute;
    left: 306px;
    width: 681px;
    top: 26px;
    margin: 0;
    text-align: center;
    white-space: nowrap;
    font-family: "Oswald", sans-serif;
    font-weight: 400;
    font-size: 82px;
    line-height: 1.2;
    letter-spacing: -0.5px;
    color: var(--text-light);
  }
  .range-card {
    position: absolute;
    left: 125px;
    top: 155px;
    width: 985px;
    height: 168px;
    background: var(--card-white);
    border-radius: 28px;
  }
  .meter-art {
    position: absolute;
    left: 9px;
    top: -35px;
    width: 80px;
    height: 168px;
    border-radius: 4px;
    background: linear-gradient(180deg, var(--art-meter-a), var(--art-meter-b));
  }
  .range-line {
    position: absolute;
    left: 90px;
    top: 36px;
    width: 863px;
    display: flex;
  }
  .range-segment {
    flex: 1;
    display: flex;
    flex-direction: column;
    align-items: center;
  }
  .range-value {
    width: 100%;
    height: 53px;
    display: flex;
    align-items: center;
    justify-content: center;
    font-family: "Roboto", sans-serif;
    font-weight: 700;
    font-size: 30px;
    color: var(--text-light);
  }
  .range-label {
    margin-top: 22px;
    font-family: "Roboto", sans-serif;
    font-weight: 700;
    font-size: 19px;
    color: var(--text-dark);
    letter-spacing: 0.3px;
  }
  .range-segment.low .range-value { background: var(--range-low); }
  .range-segment.optimal .range-value { background: var(--range-optimal); }
  .range-segment.pre-diabetic .range-value { background: var(--range-pre); }
  .range-segment.high .range-value { background: var(--range-high); }
</style>
</head>
<body>
  <main class="canvas">
    <section class="glucose-panel">
      <div class="finger-prick-art" role="img" aria-label="Illustration of a hand with a finger dripping a drop of blood"></div>
      <h1 class="panel-title">BLOOD GLUCOSE LEVEL</h1>
      <div class="range-card">
        <div class="meter-art" role="img" aria-label="Illustration of a blood glucose meter with a test strip"></div>
        <div class="range-line">
          <div class="range-segment low">
            <div class="range-value">&lt;4.0</div>
            <div class="range-label">LOW</div>
          </div>
          <div class="range-segment optimal">
            <div class="range-value">4.0 - 5.59</div>
            <div class="range-label">OPTIMAL</div>
          </div>
          <div class="range-segment pre-diabetic">
            <div class="range-value">5.6 - 6.99</div>
            <div class="range-label">PRE-DIABETIC</div>
          </div>
          <div class="range-segment high">
            <div class="range-value">&gt;=7.0</div>
            <div class="range-label">HIGH</div>
          </div>
        </div>
      </div>
    </section>
  </main>
</body>
</html>
```